Web Design Project

We are looking for a web page (home) page design for a website that offers Virtual Internet Marketing services.

The Company is called Kestrel Marketing, the services we provide are as follows:

Web Design
Social Media Management
SEO/PPC Traffic
Display
Mobile Apps
On & Offline Marketing Services

We see so many web marketing companies that struggle to produce their own great designs and call to actions. 99% of web companies do not understand marketing, so how can they help their customers drive traffic and produce sales!

We require a design that is professional yet fresh and funky! Our goal with the home page is to help prospects understand that our core business is to help them succeed and make more money, by utilising our on and offline marketing experience. We also offer done for you solutions which include - websites, design, traffic, email campaigns etc.

Included should be obvious call to actions to view our services and get our free guide/video

- A clear value proposition that identifies target audience (those that are struggling to make the web work for them)

- Easy to use navigation

We need to include an optin form where we exchange a free training guide or video series in return for an email address, above the fold to the right of the page!

We like the following to provide you with ideas:

http://www.plankhaven.com/
http://www.morvale.co.uk/
http://www.brindletopic.com/
http://www.wemplo.co.uk/ (quite like but too jumbled - too much going on)

Colours are optional, however fresh, vibrant and professional looking.

The final design should be easy on the eye, not lead to any confusion as to what we do and be simple to navigate.

Industry/Entity Type

Marketing

Requirements
Must have
• Optin form
Footer section
showcase of services offered.

```html
<!DOCTYPE html>
<html lang="en">
<head>
<meta charset="utf-8">
<title>Kestrel Marketing</title>
<link href="https://fonts.googleapis.com/css2?family=Open+Sans:wght@300;400;600;700;800&display=swap" rel="stylesheet">
<style>
:root{
  --blue:#0aa6dc;
  --blue-dark:#0580b8;
  --teal-text:#1a9fd0;
  --orange:#f7931e;
  --orange-dark:#e2680c;
  --ink:#333;
  --muted:#555;
  --red-link:#d8322b;
  --page:#ececec;
  --footer:#2b2b2b;
  --footer-line:#444;
  --green:#3cae1f;
}
*{box-sizing:border-box;margin:0;padding:0}
html,body{width:831px;height:1200px;overflow:hidden}
body{font-family:"Open Sans",Arial,sans-serif;color:var(--ink);background:var(--page);position:relative}
h1,h2,h3,h4{font-weight:400}
.abs{position:absolute}

/* header */
.site-header{left:0;top:0;width:831px;height:69px;background:linear-gradient(#fff,#f3f3f3);border-bottom:1px solid #ddd}
.logo-box{left:97px;top:0;width:184px;height:75px;background:#fff;box-shadow:0 2px 5px rgba(0,0,0,.25);z-index:2;display:flex;align-items:center;padding-left:16px;gap:10px}
.logo-mark{width:36px;height:36px;background:var(--blue)}
.logo-name{font-weight:700;font-size:17px;line-height:19px;color:#222}
.top-contact{left:500px;top:13px;font-size:9px;color:var(--teal-text)}
.main-nav{left:326px;top:34px;display:flex;align-items:center;font-size:12.5px}
.main-nav a{color:#222;text-decoration:none;padding:5px 10px}
.main-nav a.active{background:#2a2a2a;color:#fff;padding:5px 16px;border-radius:2px;margin-right:4px}
.login-btn{background:var(--green);color:#fff!important;font-size:9px;padding:2px 14px!important;border-radius:2px;margin-left:8px}

/* hero */
.hero-band{left:0;top:69px;width:831px;height:198px;background:linear-gradient(90deg,#0392cf,#17b6e8 60%,#0aa6dc)}
.hero-lower{left:0;top:267px;width:831px;height:80px;background:linear-gradient(#fff,#ececec);border-bottom:1px solid #d8d8d8}
.device-frame{left:100px;top:100px;width:283px;height:224px;background:#1b1b1b;border-radius:16px;box-shadow:0 4px 10px rgba(0,0,0,.35);padding:18px 24px}
.device-screen{width:100%;height:100%;background:linear-gradient(#fafafa,#e4e4e4)}
.hero-title{left:415px;top:96px;font-size:33px;font-weight:800;color:#fff;letter-spacing:-.5px}
.hero-sub{left:415px;top:132px;font-size:28px;font-weight:300;color:#fff}
.hero-copy{left:415px;top:166px;width:300px;font-size:11px;line-height:14px;color:#fff}
.cta-row{left:415px;top:214px;display:flex;align-items:center;gap:6px}
.cta-btn{width:96px;height:22px;background:var(--orange-dark);display:flex;align-items:center;justify-content:center;gap:4px;clip-path:polygon(0 0,100% 0,92% 50%,100% 100%,0 100%)}
.cta-btn i{width:8px;height:8px;border-radius:50%;background:#fff;display:block}
.cta-more{font-size:9px;color:#fff}
.optin-label{left:418px;top:280px;font-size:12px;color:#222}
.optin-input{left:418px;top:300px;width:215px;height:26px;background:#fff;border:1px solid #ccc;font-size:9px;color:#888;display:flex;align-items:center;padding-left:8px;gap:5px}
.mail-ico{width:10px;height:7px;border:1px solid #aaa}
.join-btn{left:637px;top:300px;width:74px;height:26px;background:linear-gradient(#ffa53a,#f07c10);color:#fff;font-weight:700;font-size:11.5px;display:flex;align-items:center;justify-content:center;border-radius:2px}

/* services */
.services-title{left:0;top:360px;width:831px;text-align:center;font-size:21px;color:#222}
.services-intro{left:100px;top:392px;width:631px;text-align:center;font-size:10.5px;line-height:13px;color:var(--muted)}
.service-card{width:178px;z-index:1}
.service-card.featured::before{content:"";position:absolute;left:-16px;top:-23px;width:206px;height:203px;background:#fff;z-index:-1}
.service-image{width:178px;height:97px;border:1px solid #ddd;background:#fff;padding:4px}
.service-image div{width:100%;height:100%}
.service-name{margin-top:13px;font-size:12.5px;color:var(--teal-text);white-space:nowrap}
.service-text{font-size:9.5px;line-height:11.5px;color:#444;margin-top:1px;height:36px;overflow:hidden}
.read-more{margin-top:6px;font-size:9.5px;color:var(--red-link)}

/* about */
.about-band{left:0;top:888px;width:831px;height:133px;background:#f6f6f4}
.about-title{left:97px;top:908px;font-size:16px;color:var(--teal-text)}
.about-text{left:97px;top:931px;width:350px;font-size:9.5px;line-height:12.5px;color:#333}
.testi-title{left:504px;top:908px;font-size:16px;color:var(--teal-text)}
.testi-arrows{left:711px;top:913px;display:flex;gap:1px}
.testi-arrows span{width:11px;height:10px;border:1px solid #bbb;background:#fff}
.testi-quote{left:504px;top:932px;width:229px;height:57px;background:#e8e8e8;padding:8px 10px;font-size:9px;line-height:11.5px;font-style:italic;color:#666}
.testi-quote::after{content:"";position:absolute;left:14px;bottom:-8px;border:8px solid transparent;border-top-color:#e8e8e8;border-bottom:0}
.testi-name{left:504px;top:990px;width:229px;text-align:right;font-size:9px;color:var(--red-link)}

/* footer */
.site-footer{left:0;top:1021px;width:831px;height:179px;background:var(--footer)}
.footer-col{top:1047px}
.footer-col h4{font-size:13px;color:var(--teal-text);margin-bottom:6px}
.footer-col li{list-style:none;font-size:8.5px;line-height:13.5px;color:#ddd}
.footer-col li.current{color:var(--orange)}
.footer-sep{top:1050px;width:1px;height:110px;background:var(--footer-line)}
.social li{display:flex;align-items:center;gap:8px;line-height:15px}
.social li i{width:10px;height:10px;background:#ddd;display:block}
.footer-contact{width:256px}
.footer-contact p{font-size:8.5px;line-height:11.5px;color:#ddd}
.footer-contact .contact-line{white-space:nowrap}
.footer-input{left:480px;top:1125px;width:170px;height:25px;background:#fff;font-size:8.5px;color:#888;display:flex;align-items:center;gap:5px;padding-left:8px}
.footer-join{left:654px;top:1125px;width:74px;height:25px}
.footer-rule{left:97px;top:1174px;width:636px;height:1px;background:#3a3a3a}
.copyright{left:97px;top:1179px;font-size:7.5px;color:#888}
</style>
</head>
<body>

<header class="site-header abs"></header>
<div class="logo-box abs"><span class="logo-mark"></span><span class="logo-name">Kestrel<br>Marketing</span></div>
<div class="top-contact abs">Phone: +108 (555) 0192 &nbsp; / &nbsp; Email: info@kestrelmarketing.com</div>
<nav class="main-nav abs">
  <a class="active">Home</a><a>About Us</a><a>Services</a><a>Cases</a><a>Blogs</a><a>Contact Us</a><a class="login-btn">Login</a>
</nav>

<section>
  <div class="hero-band abs"></div>
  <div class="hero-lower abs"></div>
  <div class="device-frame abs"><div class="device-screen" role="img" aria-label="Illustration of a tablet showing a network of social media icons being tapped by a hand"></div></div>
  <h1 class="hero-title abs">BETTER STRATEGY</h1>
  <h2 class="hero-sub abs">Social Media Management</h2>
  <p class="hero-copy abs">There are many variations of passages of Lorem Ipsum available, but the majority have suffered alteration in some form, by injected humour,</p>
  <div class="cta-row abs"><span class="cta-btn"><i></i><i></i><i></i><i></i><i></i></span><span class="cta-more">[ Read More ]</span></div>
  <p class="optin-label abs">free Signup for training guide or video series</p>
  <div class="optin-input abs"><span class="mail-ico"></span>Email Address</div>
  <div class="join-btn abs">Join Now!</div>
</section>

<section>
  <h2 class="services-title abs">Our Services</h2>
  <p class="services-intro abs">There are many variations of passages of Lorem Ipsum available, but the majority have suffered alteration in some form, by injected humour, or randomised words which don't look even slightly believable. If you are going to use a passage of Lorem Ipsum, you need to be sure there isn't anything embarrassing hidden in the middle of text.</p>

  <article class="service-card abs" style="left:97px;top:475px">
    <div class="service-image"><div role="img" aria-label="Website layouts shown in a browser" style="background:linear-gradient(135deg,#e9eef3,#4aa3d8)"></div></div>
    <h3 class="service-name">Web Design</h3>
    <p class="service-text">Lorem Ipsum available, but the majority have suffered alteration in some form, by injected humour, or randomised</p>
    <p class="read-more">Read More &raquo;</p>
  </article>
  <article class="service-card featured abs" style="left:326px;top:475px">
    <div class="service-image"><div role="img" aria-label="Social media icons floating above a phone" style="background:linear-gradient(#f2f2f2,#b9c7d3)"></div></div>
    <h3 class="service-name">Social Media Management</h3>
    <p class="service-text">by injected humour, or randomised words which don't look even slightly believable. If you are going to use a passage of</p>
    <p class="read-more">Read More &raquo;</p>
  </article>
  <article class="service-card abs" style="left:556px;top:475px">
    <div class="service-image"><div role="img" aria-label="Hand holding a smartphone with app icons" style="background:linear-gradient(90deg,#fff,#f2d7c0)"></div></div>
    <h3 class="service-name">Mobile Apps</h3>
    <p class="service-text">Lorem Ipsum available, but the majority have suffered alteration in some form, by injected humour,</p>
    <p class="read-more">Read More &raquo;</p>
  </article>

  <article class="service-card abs" style="left:97px;top:686px">
    <div class="service-image"><div role="img" aria-label="Cartoon presenter next to a rising traffic chart" style="background:linear-gradient(90deg,#f4f4f4,#f3d6a8)"></div></div>
    <h3 class="service-name">SEO/PPC Traffic</h3>
    <p class="service-text">Lorem Ipsum available, but the majority have suffered alteration in some form, by injected humour, or randomised</p>
    <p class="read-more">Read More &raquo;</p>
  </article>
  <article class="service-card abs" style="left:326px;top:686px">
    <div class="service-image"><div role="img" aria-label="Thumbs down and thumbs up beside bar charts" style="background:linear-gradient(90deg,#e8e8e8,#6c6c6c,#e8e8e8)"></div></div>
    <h3 class="service-name">On &amp; Offline Marketing Services</h3>
    <p class="service-text">by injected humour, or randomised words which don't look even slightly believable. If you are going to use a passage of</p>
    <p class="read-more">Read More &raquo;</p>
  </article>
  <article class="service-card abs" style="left:556px;top:686px">
    <div class="service-image"><div role="img" aria-label="Monitor, laptop, tablet and phone displaying ads" style="background:linear-gradient(#f4f4f4,#8a8f96)"></div></div>
    <h3 class="service-name">Display</h3>
    <p class="service-text">Lorem Ipsum available, but the majority have suffered alteration in some form, by injected humour,</p>
    <p class="read-more">Read More &raquo;</p>
  </article>
</section>

<section>
  <div class="about-band abs"></div>
  <h2 class="about-title abs">Who we are?</h2>
  <p class="about-text abs">There are many variations of passages of Lorem Ipsum available, but the majority have suffered alteration in some form, by injected humour, or randomised words which don't look even slightly believable. If you are going to use a passage of Lorem Ipsum, you need to be sure there isn't anything embarrassing hidden in the middle of text.</p>
  <h2 class="testi-title abs">Testimonials</h2>
  <div class="testi-arrows abs"><span></span><span></span></div>
  <blockquote class="testi-quote abs">There are many variations of passages of Lorem Ipsum available, but the majority have suffered alteration in some form, by injected</blockquote>
  <p class="testi-name abs">[ Daniel Hartwell Moore ]</p>
</section>

<footer>
  <div class="site-footer abs"></div>
  <div class="footer-col abs" style="left:98px"><h4>Site Map</h4><ul><li>Home</li><li>About Us</li><li>Services</li><li>Cases</li><li>Blogs</li><li>Contact Us</li></ul></div>
  <div class="footer-sep abs" style="left:175px"></div>
  <div class="footer-col abs" style="left:192px"><h4>Our Services</h4><ul><li>Web Design</li><li>Social Media Management</li><li class="current">SEO/PPC Traffic</li><li>Display</li><li>Mobile Apps</li><li>On &amp; Offline Marketing Services</li></ul></div>
  <div class="footer-sep abs" style="left:330px"></div>
  <div class="footer-col social abs" style="left:357px"><h4>Social Media</h4><ul><li><i></i>RSS Feed</li><li><i></i>Friendspace</li><li><i></i>Chirper</li><li><i></i>Linkhub</li><li><i></i>Circlesphere</li></ul></div>
  <div class="footer-sep abs" style="left:457px"></div>
  <div class="footer-col footer-contact abs" style="left:480px"><h4>Contact Us</h4><p>It is a long established fact that a reader will be distracted by the readable content of a page when looking at its layout.</p><p class="contact-line">Phone: +108 (555) 0192 &nbsp;/&nbsp; Email: info@kestrelmarketing.com</p></div>
  <div class="footer-input abs"><span class="mail-ico"></span>Drop your E-mail here</div>
  <div class="join-btn footer-join abs">Join Now!</div>
  <div class="footer-rule abs"></div>
  <p class="copyright abs">&copy; 2013 kestrelmarketing.com. All Rights Reserved.</p>
</footer>

</body>
</html>
```